Design Business Cards

MV construction is a construction company. business card should have:
- License #
- position
- name
- cell #
- office #
- website
any other ideas are welcome!

```html
<!DOCTYPE html>
<html lang="en">
<head>
<meta charset="utf-8">
<title>MV Construction – Business Cards</title>
<link href="https://fonts.googleapis.com/css2?family=Montserrat:wght@400;500;700;800&display=swap" rel="stylesheet">
<style>
  :root {
    --backdrop: #e7ebeb;
    --card: #ffffff;
    --ink: #141414;
    --muted: #3a3a3a;
    --gold: #c9a01c;
    --faint: #ececec;
    --rule: #9a9a9a;
  }
  * { box-sizing: border-box; margin: 0; padding: 0; }
  html, body {
    width: 1200px; height: 900px; overflow: hidden;
    background: var(--backdrop);
    font-family: "Montserrat", sans-serif;
  }
  .sheet {
    width: 1200px; height: 900px;
    display: flex; flex-direction: column; align-items: center; justify-content: center;
    gap: 40px;
  }
  .card {
    position: relative;
    width: 700px; height: 400px;
    background: var(--card);
    box-shadow: 0 6px 18px rgba(0,0,0,0.12);
    overflow: hidden;
  }

  /* Contact side */
  .card-contact .faint-name {
    position: absolute; right: 40px; bottom: 70px;
    font-weight: 800; font-size: 44px; letter-spacing: 6px;
    color: var(--faint);
  }
  .person {
    position: absolute; left: 70px; top: 170px; width: 230px;
    text-align: right;
  }
  .person-name {
    font-weight: 800; font-size: 28px; letter-spacing: 1px; color: var(--ink);
  }
  .person-role {
    font-weight: 400; font-size: 17px; color: var(--muted); margin-top: 2px;
  }
  .divider {
    position: absolute; left: 320px; top: 110px; width: 1.5px; height: 180px;
    background: var(--rule);
  }
  .contact-list {
    position: absolute; left: 340px; top: 110px;
    list-style: none;
  }
  .contact-list li {
    display: flex; align-items: center; gap: 10px;
    height: 36px;
    font-size: 18px; font-weight: 500; color: var(--ink);
  }
  .contact-list svg { width: 22px; height: 22px; flex: none; }

  /* Brand side */
  .card-brand {
    display: flex; flex-direction: column; align-items: center; justify-content: center;
  }
  .brand-name {
    display: flex; align-items: center; gap: 14px;
    font-weight: 800; font-size: 46px; letter-spacing: 4px; color: var(--gold);
  }
  .brand-mark { width: 22px; height: 22px; background: var(--ink); }
  .brand-web {
    margin-top: 22px;
    font-weight: 500; font-size: 19px; color: var(--ink); letter-spacing: 0.5px;
  }
</style>
</head>
<body>
<main class="sheet">

  <section class="card card-contact" aria-label="Business card contact side">
    <div class="faint-name" aria-hidden="true">MV CONSTRUCTION</div>
    <div class="person">
      <div class="person-name">DANIEL MORROW</div>
      <div class="person-role">Manager</div>
    </div>
    <div class="divider"></div>
    <ul class="contact-list">
      <li>
        <svg viewBox="0 0 24 24" fill="none" stroke="#141414" stroke-width="1.8"><circle cx="12" cy="12" r="10"/><path d="M9 8v8M15 8v8M7 10.5h10M7 13.5h10"/></svg>
        LIC 482193
      </li>
      <li>
        <svg viewBox="0 0 24 24" fill="none" stroke="#141414" stroke-width="1.8"><circle cx="12" cy="12" r="10"/><path d="M8.5 7.5l2 2-1.2 1.5a6 6 0 0 0 3.7 3.7l1.5-1.2 2 2-1.5 1.5c-4 0-8-4-8-8z"/></svg>
        0400 555 218
      </li>
      <li>
        <svg viewBox="0 0 24 24" fill="none" stroke="#141414" stroke-width="1.8"><circle cx="12" cy="12" r="10"/><rect x="7" y="8.5" width="10" height="7"/><path d="M7 8.5l5 4 5-4"/></svg>
        info@mvbuild.com.au
      </li>
      <li>
        <svg viewBox="0 0 24 24" fill="none" stroke="#141414" stroke-width="1.8"><circle cx="12" cy="12" r="10"/><circle cx="12" cy="12" r="5"/><path d="M7 12h10M12 7c-2 3-2 7 0 10M12 7c2 3 2 7 0 10"/></svg>
        www.mvbuild.com.au
      </li>
      <li>
        <svg viewBox="0 0 24 24" fill="none" stroke="#141414" stroke-width="1.8"><circle cx="12" cy="12" r="10"/><path d="M12 18s-4-4-4-7a4 4 0 0 1 8 0c0 3-4 7-4 7z"/><circle cx="12" cy="11" r="1.3"/></svg>
        14 Harbour Road, VIC 3141
      </li>
    </ul>
  </section>

  <section class="card card-brand" aria-label="Business card brand side">
    <div class="brand-name"><span class="brand-mark"></span>MV CONSTRUCTION</div>
    <div class="brand-web">www.mvbuild.com.au</div>
  </section>

</main>
</body>
</html>
```